Professional Business Cards for Recruiting Company

We'd like professional 2-sided business cards that reflect a color scheme that matches our website, www.queryvantline.com, and / or logo that is attached.

Slogan used is "We Know People", but needs to be editable because we change it up to "We Know Developers", "We Speak Geek", etc.

Must includes logo, slogan, first and last name, address, email, mobile number and website address.

Files attached for ideas.

Thanks!

Contact Information for Business Card

Logo, Company name, First name, Last name, addresss, email, phone, website address.

Font styles to use
Sans Serif

Colors
0054AA
0677BA
7BADD7
CADEEF
E8F1F8

Requirements
Nice to have
• I do like the following designs. 22962062 and 22962651. Couple ideas anyway.

```html
<!DOCTYPE html>
<html lang="en">
<head>
<meta charset="utf-8">
<title>Queryvantline Business Cards</title>
<link rel="stylesheet" href="https://fonts.googleapis.com/css2?family=Montserrat:wght@300;400;600;700&family=Roboto:wght@300;400&display=swap">
<style>
  :root {
    --bg: #e9e9ea;
    --card-white: #ffffff;
    --card-dark: #2b2b2c;
    --card-dark-2: #3a3a3b;
    --brand-blue: #0054aa;
    --brand-mid: #0677ba;
    --text-gray: #6b6b6b;
    --slogan-light: #d8d8d8;
    --photo-1: #e6ebf3;
    --photo-2: #b9c6d8;
  }
  * { box-sizing: border-box; margin: 0; padding: 0; }
  html, body { width: 1200px; height: 802px; overflow: hidden; }
  body {
    background: var(--bg);
    font-family: "Montserrat", sans-serif;
    position: relative;
  }
  .card {
    position: absolute;
    top: 246px;
    width: 540px;
    height: 309px;
    border-bottom: 3px solid var(--brand-blue);
    box-shadow: 0 10px 24px rgba(0,0,0,0.18);
    overflow: hidden;
  }
  .card--front { left: 45px; background: var(--card-white); }
  .card--back { left: 615px; background: var(--card-dark); }

  /* front */
  .portrait {
    position: absolute;
    left: 0; bottom: 0;
    width: 210px; height: 309px;
    background: linear-gradient(160deg, var(--photo-1), var(--photo-2));
  }
  .front-content {
    position: absolute;
    left: 235px; top: 34px; right: 28px;
  }
  .brand {
    display: flex;
    align-items: center;
    gap: 12px;
  }
  .brand-square {
    width: 34px; height: 34px;
    border: 2px solid var(--brand-blue);
    flex: none;
  }
  .brand-text { display: flex; flex-direction: column; }
  .brand-name {
    font-weight: 300;
    font-size: 25px;
    letter-spacing: 1px;
    color: var(--brand-blue);
    line-height: 1;
    border-bottom: 1.5px solid var(--brand-blue);
    padding-bottom: 3px;
  }
  .brand-slogan {
    font-size: 7px;
    font-weight: 600;
    letter-spacing: 1.6px;
    color: var(--text-gray);
    text-transform: uppercase;
    margin-top: 4px;
  }
  .person { margin-top: 30px; }
  .person-name {
    font-weight: 700;
    font-size: 19px;
    color: var(--brand-blue);
    letter-spacing: 0.5px;
    text-transform: uppercase;
  }
  .person-title {
    font-family: "Roboto", sans-serif;
    font-weight: 300;
    font-size: 14px;
    color: var(--text-gray);
    margin-top: 2px;
  }
  .address {
    font-family: "Roboto", sans-serif;
    font-weight: 300;
    font-size: 13px;
    color: var(--text-gray);
    line-height: 1.3;
    margin-top: 18px;
  }
  .contacts {
    list-style: none;
    margin-top: 16px;
    font-family: "Roboto", sans-serif;
    font-weight: 300;
    font-size: 13px;
    color: var(--text-gray);
  }
  .contacts li {
    display: flex;
    align-items: center;
    gap: 8px;
    line-height: 1.45;
  }
  .contacts svg { width: 11px; height: 11px; flex: none; }

  /* back */
  .back-pattern {
    position: absolute;
    inset: 0;
    background: radial-gradient(ellipse at 60% 40%, var(--card-dark-2), var(--card-dark) 70%);
  }
  .back-brand {
    position: absolute;
    left: 150px; top: 128px;
    display: flex;
    align-items: center;
    gap: 14px;
  }
  .back-square {
    width: 44px; height: 44px;
    border: 2.5px solid #ffffff;
    flex: none;
  }
  .back-brand .brand-name {
    font-size: 28px;
    color: var(--brand-mid);
    border-bottom-color: var(--brand-mid);
  }
  .back-brand .brand-slogan { color: var(--slogan-light); font-size: 7.5px; }
</style>
</head>
<body>
  <section class="card card--front">
    <div class="portrait" role="img" aria-label="Portrait photo of the card holder in a light shirt and dark tie"></div>
    <div class="front-content">
      <div class="brand">
        <span class="brand-square"></span>
        <div class="brand-text">
          <span class="brand-name">QUERYVANTLINE</span>
          <span class="brand-slogan">We Know People</span>
        </div>
      </div>
      <div class="person">
        <div class="person-name">Daniel Mercer</div>
        <div class="person-title">Manager</div>
      </div>
      <div class="address">Your address, city<br>state, ZIP 0000</div>
      <ul class="contacts">
        <li>
          <svg viewBox="0 0 12 12"><path d="M3 1 L5 3.5 L4 4.8 C4.8 6.4 5.6 7.2 7.2 8 L8.5 7 L11 9 L9.6 11 C5 10.6 1.4 7 1 2.4 Z" fill="var(--brand-blue)"/></svg>
          555-014-2298
        </li>
        <li>
          <svg viewBox="0 0 12 12"><rect x="1" y="2.5" width="10" height="7" fill="none" stroke="var(--brand-blue)" stroke-width="1.2"/><path d="M1 2.5 L6 6.5 L11 2.5" fill="none" stroke="var(--brand-blue)" stroke-width="1.2"/></svg>
          info@queryvantline.com
        </li>
        <li>
          <svg viewBox="0 0 12 12"><circle cx="6" cy="6" r="5" fill="none" stroke="var(--brand-blue)" stroke-width="1.1"/><ellipse cx="6" cy="6" rx="2.2" ry="5" fill="none" stroke="var(--brand-blue)" stroke-width="1"/><path d="M1 6 H11 M2 3.5 H10 M2 8.5 H10" stroke="var(--brand-blue)" stroke-width="0.9"/></svg>
          www.queryvantline.com
        </li>
      </ul>
    </div>
  </section>

  <section class="card card--back">
    <div class="back-pattern" role="img" aria-label="Embossed repeating brand pattern on dark charcoal"></div>
    <div class="back-brand">
      <span class="back-square"></span>
      <div class="brand-text">
        <span class="brand-name">QUERYVANTLINE</span>
        <span class="brand-slogan">We Know People</span>
      </div>
    </div>
  </section>
</body>
</html>
```